Promotional brochure for VoIP service

Need a flyer to promote our VoIP service. We are offering a free phone per line for signup with 2 year contract. List features. Prices are $24.99/Line, free mobile app.

Target Market(s)

Businesses

Font styles to use
Sans Serif

Colors
7da6d0

Requirements
Must have
• logo and picture of phone. Disclaimer on free phone offer "2 year contract requires. Phone shown is not actual phone. Free phone will be refurbished Quorvex M48 or equivalent. You have an option to apply $30 credit to new phone purchase."
Nice to have
• Same color scheme as attached brochure.

```html
<!DOCTYPE html>
<html lang="en">
<head>
<meta charset="utf-8">
<title>Talonis VOIP – Free Phone Flyer</title>
<link rel="stylesheet" href="https://fonts.googleapis.com/css2?family=Montserrat:wght@600;700;800;900&family=Oswald:wght@500;600&family=Open+Sans:wght@400;600&display=swap">
<style>
  :root{
    --brand-blue:#0b4f96;
    --brand-blue-deep:#084282;
    --sky:#7da6d0;
    --slate:#6b6e73;
    --alert-red:#e8323f;
    --paper:#ffffff;
    --mist:#f1f2f4;
    --footer-grey:#dcdde0;
    --stage:#e6e6e6;
  }
  *{box-sizing:border-box;margin:0;padding:0}
  html,body{width:1200px;height:986px;overflow:hidden;background:var(--stage)}
  .flyer{
    position:absolute;left:255px;top:28px;width:690px;height:930px;
    background:linear-gradient(180deg,var(--paper) 0%,var(--paper) 60%,var(--mist) 100%);
    overflow:hidden;font-family:"Open Sans",sans-serif;
    box-shadow:0 6px 24px rgba(0,0,0,.12);
  }
  .headline{position:absolute;left:0;right:40px;top:30px;text-align:right}
  .headline__title{
    font-family:"Montserrat",sans-serif;font-weight:900;color:var(--brand-blue);
    font-size:92px;line-height:1;letter-spacing:1px;
  }
  .headline__sub{
    font-family:"Montserrat",sans-serif;font-weight:800;color:var(--slate);
    font-size:27px;line-height:1.15;margin-top:4px;letter-spacing:.5px;
  }
  .hero-photo{
    position:absolute;left:0;top:190px;width:690px;height:380px;
    background:
      linear-gradient(180deg,rgba(255,255,255,0) 70%,rgba(196,150,104,.55) 100%),
      linear-gradient(100deg,#d9d7d3 0%,#f4f2ee 40%,#faf7f2 65%,#e8e2d8 100%);
  }
  .tagline-band{position:absolute;left:0;top:470px;width:690px;height:150px}
  .tagline-band__text{
    position:absolute;left:90px;top:512px;width:560px;
    font-family:"Montserrat",sans-serif;font-weight:700;color:#fff;
    font-size:19px;line-height:1.3;text-align:center;letter-spacing:.6px;
  }
  .decor-curves{position:absolute;left:0;top:560px;width:690px;height:370px}
  .features{position:absolute;left:60px;top:640px}
  .features__title{
    font-family:"Montserrat",sans-serif;font-weight:700;color:var(--brand-blue);font-size:21px;
  }
  .features__list{list-style:none;margin-top:4px}
  .features__list li{
    font-size:15px;color:var(--brand-blue);line-height:1.4;padding-left:18px;position:relative;
  }
  .features__list li::before{content:"";position:absolute;left:2px;top:9px;width:5px;height:5px;border-radius:50%;background:var(--brand-blue)}
  .brand{position:absolute;left:60px;top:762px;display:flex;align-items:center;gap:12px}
  .brand__dot{width:22px;height:22px;border-radius:50%;background:var(--sky)}
  .brand__name{font-family:"Open Sans",sans-serif;font-weight:600;font-size:36px;color:var(--brand-blue)}
  .footer{
    position:absolute;left:0;bottom:0;width:690px;height:106px;background:var(--footer-grey);
    padding:10px 40px 0 60px;
  }
  .footer__url{font-family:"Montserrat",sans-serif;font-weight:800;color:var(--brand-blue);font-size:22px;letter-spacing:.5px}
  .footer__tag{font-family:"Montserrat",sans-serif;font-weight:600;color:var(--brand-blue);font-size:14px;letter-spacing:.8px;margin-top:2px}
  .footer__disclaimer{font-size:9.5px;line-height:1.35;color:var(--slate);margin-top:6px}
  .price-badge{position:absolute;left:376px;top:606px;width:310px;height:210px;transform:rotate(-5deg)}
  .price-badge svg{position:absolute;left:0;top:0}
  .price-badge__text{
    position:absolute;left:30px;top:70px;font-family:"Oswald",sans-serif;font-weight:600;color:#fff;line-height:1;
  }
  .price-badge__label{font-size:28px;letter-spacing:.5px}
  .price-badge__price{font-size:44px;margin-top:6px}
  .app-tag{
    position:absolute;left:222px;top:28px;width:86px;height:72px;background:var(--alert-red);
    color:#fff;font-family:"Montserrat",sans-serif;font-weight:800;font-size:15px;line-height:1.05;
    display:flex;align-items:center;justify-content:center;text-align:center;
  }
</style>
</head>
<body>
<main class="flyer">
  <header class="headline">
    <h1 class="headline__title">FREE PHONE</h1>
    <p class="headline__sub">PER LINE FOR SIGNUP WITH<br>2 YEAR CONTRACT.</p>
  </header>

  <div class="hero-photo" role="img" aria-label="Photo of a businessman's hand lifting the handset of a black office desk phone on a wooden desk"></div>

  <svg class="tagline-band" viewBox="0 0 690 150" aria-hidden="true">
    <polygon points="90,32 650,18 640,95 110,118" fill="#0b4f96"/>
    <polygon points="60,40 90,32 110,118 75,120" fill="#084282"/>
  </svg>
  <p class="tagline-band__text">DELIVERING EXCEPTIONAL UNIFIED<br>COMMUNICATIONS AND COLLABORATION</p>

  <svg class="decor-curves" viewBox="0 0 690 370" aria-hidden="true">
    <path d="M440 0 C560 80 600 220 520 370" fill="none" stroke="#ffffff" stroke-width="6"/>
    <path d="M470 0 C590 90 620 230 545 370" fill="none" stroke="#e4e6ea" stroke-width="3"/>
    <path d="M300 370 C420 300 560 300 690 340" fill="none" stroke="#ffffff" stroke-width="5"/>
  </svg>

  <section class="features">
    <h2 class="features__title">List Features</h2>
    <ul class="features__list">
      <li>Business Voice Solutions</li>
      <li>Rich Suite of UCC Services</li>
      <li>Custom Installation, Delivery &amp; Support</li>
      <li>Unparalleled Service Uptime</li>
    </ul>
  </section>

  <div class="price-badge">
    <svg width="310" height="210" viewBox="0 0 310 210" aria-hidden="true">
      <rect x="26" y="8" width="262" height="186" fill="none" stroke="#8a8c90" stroke-width="2"/>
      <polygon points="40,185 210,176 170,208" fill="#0b4f96"/>
      <polygon points="150,152 260,152 238,190 150,190" fill="#6b6e73"/>
      <polygon points="0,42 310,20 310,150 18,176" fill="#0b4f96"/>
      <line x1="0" y1="45" x2="220" y2="30" stroke="#e8323f" stroke-width="1.5" stroke-dasharray="3 3"/>
      <line x1="6" y1="58" x2="16" y2="168" stroke="#e8323f" stroke-width="1.5" stroke-dasharray="3 3"/>
    </svg>
    <div class="price-badge__text">
      <div class="price-badge__label">PRICES ARE</div>
      <div class="price-badge__price">$24.99/LINE</div>
    </div>
    <div class="app-tag">FREE<br>MOBILE<br>APP</div>
  </div>

  <div class="brand">
    <span class="brand__dot"></span>
    <span class="brand__name">Talonis VOIP</span>
  </div>

  <footer class="footer">
    <div class="footer__url">WWW.TALONISVOIP.COM</div>
    <div class="footer__tag">UNIFIED COMMUNICATIONS AT WORK</div>
    <p class="footer__disclaimer">2 year contract required. Phone shown is not actual phone. Free phone will be refurbished Quorvex M48 or equivalent. You have an option to apply $30 credit to new phone purchase.</p>
  </footer>
</main>
</body>
</html>
```